Thriving Mexican import business needs a new business card

Need a refresher of our current business card. Looking for a lighter background with the logo on one side. We will want this file to be adjustable so we can change names, emails and mobile numbers.
We are open to ideas but maintaining a professional image is critical.
Thankyou,

Target Market(s)

Anyone in food industry

Industry/Entity Type

Wholesale

Contact Information for Business Card

Mark Pendlebury
Director
Condor Provisions & Spirits Pty Ltd
5B Morrow Ct, Kelvinbrook VIC 3127
0421930576 (03) 95128460
mark@condorlatino.example.au
condorlatinoprovisionsandspirits.example.au

Font styles to use
Serif
Other font styles liked:
• NeoGram Heavy

Requirements
Must have
• Professional yet memorable
Condor logo
Nice to have
• Chilli or tequila/mexican food pictures
Should not have
• Dark background

```html
<!DOCTYPE html>
<html lang="en">
<head>
<meta charset="utf-8">
<title>Condor Business Card</title>
<link rel="stylesheet" href="https://fonts.googleapis.com/css2?family=Bebas+Neue&family=Open+Sans:wght@400;700&display=swap">
<style>
  :root {
    --backdrop: #d6d6d6;
    --card: #ffffff;
    --ink: #111111;
    --body-ink: #222222;
    --emblem-light: #ececec;
    --emblem-mid: #dedede;
  }
  * { margin: 0; padding: 0; box-sizing: border-box; }
  html, body {
    width: 1200px; height: 900px; overflow: hidden;
    background: var(--backdrop);
  }
  .canvas { position: relative; width: 1200px; height: 900px; }

  .card {
    position: absolute; top: 217px; width: 309px; height: 500px;
    background: var(--card); overflow: hidden;
    box-shadow: 0 2px 6px rgba(0,0,0,0.25);
  }
  .card--front { left: 279px; border-radius: 0 60px 0 60px; }
  .card--back  { left: 617px; border-radius: 60px 0 60px 0; }

  .emblem-backdrop {
    position: absolute; inset: 0;
    background: linear-gradient(160deg, var(--emblem-mid) 0%, var(--emblem-light) 45%, var(--card) 55%, var(--emblem-light) 75%, var(--emblem-mid) 100%);
  }

  .wordmark {
    position: absolute; left: 0; right: 0; text-align: center;
    font-family: "Open Sans", sans-serif; font-weight: 700;
    font-size: 46px; line-height: 1; letter-spacing: 2px;
    color: var(--ink);
  }
  .card--front .wordmark { top: 226px; }
  .card--back .wordmark { top: 132px; }

  .contact {
    position: absolute; left: 28px; right: 10px; top: 318px;
    font-family: "Open Sans", sans-serif; color: var(--body-ink);
  }
  .contact__name {
    font-family: "Bebas Neue", sans-serif; font-size: 22px; line-height: 1; color: var(--ink);
  }
  .contact__role { font-size: 12.5px; margin-top: 2px; }
  .contact__list { list-style: none; margin-top: 12px; }
  .contact__item {
    display: flex; align-items: center; gap: 4px;
    font-size: 12.5px; line-height: 18px; white-space: nowrap;
  }
  .contact__item--web { font-size: 11px; }
  .contact__icon { width: 13px; height: 13px; flex: none; }
  .company { margin-top: 12px; }
  .company__name { font-weight: 700; font-size: 12.5px; line-height: 18px; }
  .company__address { font-size: 12.5px; line-height: 18px; }
</style>
</head>
<body>
<div class="canvas">

  <section class="card card--front">
    <div class="emblem-backdrop" role="img" aria-label="Large faint brand emblem pattern in light grey"></div>
    <div class="wordmark">CONDOR</div>
  </section>

  <section class="card card--back">
    <div class="wordmark">CONDOR</div>

    <div class="contact">
      <div class="contact__name">MARK PENDLEBURY</div>
      <div class="contact__role">Director</div>
      <ul class="contact__list">
        <li class="contact__item">
          <svg class="contact__icon" viewBox="0 0 24 24" aria-hidden="true"><path fill="#111" d="M6.6 10.8a15.2 15.2 0 0 0 6.6 6.6l2.2-2.2c.3-.3.7-.4 1-.2 1.1.4 2.3.6 3.6.6.6 0 1 .4 1 1V20c0 .6-.4 1-1 1A17 17 0 0 1 3 4c0-.6.4-1 1-1h3.5c.6 0 1 .4 1 1 0 1.3.2 2.5.6 3.6.1.3 0 .7-.2 1z"/></svg>
          0421930576 (03) 95128460
        </li>
        <li class="contact__item">
          <svg class="contact__icon" viewBox="0 0 24 24" aria-hidden="true"><path fill="#111" d="M2 5h20v14H2z"/><path d="M2 5l10 8 10-8" fill="none" stroke="#fff" stroke-width="2"/></svg>
          mark@condorlatino.example.au
        </li>
        <li class="contact__item contact__item--web">
          <svg class="contact__icon" viewBox="0 0 24 24" aria-hidden="true"><g fill="none" stroke="#111" stroke-width="2"><circle cx="12" cy="12" r="10"/><ellipse cx="12" cy="12" rx="4.5" ry="10"/><path d="M2 12h20M4 7h16M4 17h16"/></g></svg>
          condorlatinoprovisionsandspirits.example.au
        </li>
      </ul>
      <div class="company">
        <div class="company__name">CONDOR PROVISIONS &amp; SPIRITS PTY LTD</div>
        <div class="company__address">5B Morrow Ct, Kelvinbrook VIC 3127</div>
      </div>
    </div>
  </section>

</div>
</body>
</html>
```